Home page for Mira Talk Hub

Develop the home page for MiraTalkHub.co, which is an AI-powered chatbot platform that allows users to add an educated chatbot to their websites to assist customers with questions and other inquiries.

The hero banner should contain the text:

"Instantly create a FREE AI Chatbot for your website! Just enter the URL of your website below and the chatbot will educate itself about your business"

Below this text should be an text box to enter the URL of the visitor's website.

The platform is a subsidiary of KorvanPro.com, so the theme should be very similar to the website korvanpro.com.

I have attached the content for the page, a mockup of the hero banner section, and videos for the hero banner.

```html
<!DOCTYPE html>
<html lang="en">
<head>
<meta charset="UTF-8">
<title>Mira Talk Hub — Free AI Chatbot</title>
<link href="https://fonts.googleapis.com/css2?family=Oswald:wght@500;700&family=Poppins:ital,wght@0,400;0,500;0,600;1,400&display=swap" rel="stylesheet">
<style>
:root{
  --navy:#061a33;
  --navy-deep:#030f22;
  --navy-mid:#0b2a4d;
  --blue:#1ea0e6;
  --blue-light:#43b8f2;
  --ink:#1b1f27;
  --muted:#5b6270;
  --card:#ececec;
  --gray-band:#e6e6e6;
  --faq-open:#e4edf5;
  --white:#ffffff;
}
*{margin:0;padding:0;box-sizing:border-box}
html,body{width:1200px;height:5036px;overflow:hidden}
body{font-family:'Poppins',sans-serif;color:var(--ink);background:var(--white);position:relative}
h1,h2,h3,.logo{font-family:'Oswald',sans-serif;text-transform:uppercase;font-weight:700}
.btn{display:inline-block;background:var(--blue);color:var(--white);border-radius:30px;font-size:14px;font-weight:500;padding:12px 30px}
section,header,footer{position:relative;width:1200px;overflow:hidden}

/* Hero */
.hero{height:760px;background:linear-gradient(100deg,var(--navy-deep) 0%,var(--navy-mid) 55%,#123b63 100%)}
.hero-visual{position:absolute;left:520px;top:0;width:680px;height:760px;background:radial-gradient(ellipse at 60% 50%,#5a7590 0%,#2a4764 40%,rgba(11,42,77,0) 75%)}
.nav{position:absolute;top:26px;left:80px;right:80px;display:flex;align-items:center}
.logo{color:var(--white);font-size:26px;letter-spacing:.5px;white-space:nowrap}
.nav-links{display:flex;gap:44px;margin-left:auto;margin-right:34px;color:var(--white);font-size:15px;font-weight:500}
.login{display:flex;align-items:center;gap:10px;background:var(--blue);color:var(--white);border-radius:26px;padding:8px 24px 8px 10px;font-size:15px;font-weight:500}
.login i{width:22px;height:22px;border-radius:50%;background:var(--white);display:block}
.hero h1{position:absolute;left:80px;top:160px;width:540px;color:var(--white);font-size:60px;line-height:1.05}
.hero p{position:absolute;left:80px;top:310px;width:440px;color:#dce6f0;font-size:15px;line-height:1.55}
.url-box{position:absolute;left:80px;top:432px;width:430px;height:40px;border-radius:22px;background:var(--white);color:#8a909a;font-size:13px;padding:11px 22px}
.hero .btn{position:absolute;left:80px;top:500px}
.hero-curve{position:absolute;left:0;bottom:0}

/* Welcome */
.welcome{height:500px}
.welcome-photo{position:absolute;left:132px;top:180px;width:460px;height:260px;border-radius:22px;background:linear-gradient(135deg,#3b2a22,#8a5a3c 50%,#2a3340)}
.welcome h2{position:absolute;left:640px;top:188px;font-size:34px;white-space:nowrap}
.welcome p{position:absolute;left:640px;top:240px;width:460px;font-size:12px;line-height:1.55;color:var(--muted)}
.welcome .btn{position:absolute;left:640px;top:384px}

/* How it works */
.how{height:560px;text-align:center}
.how h2{position:absolute;top:40px;width:100%;font-size:42px}
.how .lead{position:absolute;top:100px;left:280px;width:640px;font-size:12px;line-height:1.55;color:var(--muted)}
.how-cards{position:absolute;top:162px;left:168px;display:flex;gap:24px}
.how-card{width:272px;height:220px;background:var(--card);border-radius:22px;position:relative;padding:82px 28px 0}
.how-card .tab{position:absolute;top:0;left:86px;width:100px;height:30px;background:var(--white);border-radius:0 0 18px 18px}
.how-card h3{font-size:20px;margin-bottom:8px}
.how-card p{font-size:12.5px;line-height:1.55;color:var(--muted)}
.how .btn{position:absolute;top:432px;left:538px}

/* Why / plans dark */
.why{height:940px;background:linear-gradient(180deg,var(--navy) 0%,#0a2646 50%,var(--navy) 100%)}
.why .why-title{position:absolute;left:132px;top:140px;color:var(--white);font-size:36px;white-space:nowrap}
.why .intro{position:absolute;left:132px;top:196px;width:420px;color:#cfd9e4;font-size:13px;line-height:1.6}
.why ul{position:absolute;left:132px;top:258px;list-style:none;color:#cfd9e4;font-size:13px;line-height:1.9}
.why ul li::before{content:"•";color:var(--blue-light);margin-right:10px}
.why .btn{position:absolute;left:132px;top:356px}
.why-photo{position:absolute;left:608px;top:60px;width:452px;height:380px;border-radius:22px;background:linear-gradient(135deg,#c9ccd0,#8f9aa6 55%,#4d5a69)}
.why .plans-title{position:absolute;left:0;top:530px;width:100%;text-align:center;color:var(--white);font-size:42px}
.why .plans-sub{position:absolute;left:0;top:590px;width:100%;text-align:center;color:#cfd9e4;font-size:13px}
.plan-cards{position:absolute;top:628px;left:168px;display:flex;gap:24px}
.plan-card{width:272px;height:220px;background:var(--white);border-radius:22px;text-align:center;padding:70px 30px 0;position:relative}
.plan-card .icon{position:absolute;top:26px;left:118px;width:36px;height:32px;border-radius:8px;background:var(--blue)}
.plan-card h3{font-size:22px;margin-bottom:6px}
.plan-card p{font-size:12.5px;line-height:1.55;color:var(--muted)}

/* Feature tiles */
.features{height:500px}
.features h2{position:absolute;top:56px;width:100%;text-align:center;font-size:42px}
.tile{position:absolute;top:120px;width:460px;height:320px;border-radius:22px;overflow:hidden}
.tile-a{left:132px;background:linear-gradient(160deg,#b06a2c,#5a3a22 55%,#0d1a2b 100%)}
.tile-b{left:608px;background:linear-gradient(160deg,#d6b74a,#4b6a7e 50%,#0d1a2b 100%)}
.tile .shade{position:absolute;left:0;right:0;bottom:0;height:130px;background:linear-gradient(180deg,rgba(6,26,51,0),rgba(6,26,51,.95))}
.tile h3{position:absolute;left:28px;bottom:56px;color:var(--white);font-size:20px}
.tile p{position:absolute;left:28px;bottom:16px;width:404px;color:#dbe4ee;font-size:12px;line-height:1.5}

/* Try free */
.try{height:600px;background:var(--gray-band)}
.try-photo{position:absolute;left:0;top:40px;width:560px;height:560px;background:linear-gradient(135deg,#c8cfd3,#7f8d8f 45%,#3b4a48)}
.try h2{position:absolute;left:632px;top:180px;font-size:32px;white-space:nowrap}
.try p{position:absolute;left:632px;width:460px;font-size:12.5px;line-height:1.6;color:var(--muted)}
.try .p1{top:236px}
.try .p2{top:336px}
.try .btn{position:absolute;left:632px;top:420px}

/* FAQ */
.faq{height:410px}
.faq h2{position:absolute;top:20px;width:100%;text-align:center;font-size:42px}
.faq-list{position:absolute;top:92px;left:240px;width:720px}
.faq-item{border-radius:12px;padding:12px 22px;margin-bottom:12px;display:flex;justify-content:space-between;align-items:center;gap:16px;background:#f1f4f7}
.faq-item.open{background:var(--faq-open);display:block}
.faq-q{font-family:'Oswald',sans-serif;font-weight:500;font-size:14px;text-transform:uppercase;display:flex;justify-content:space-between;align-items:center}
.faq-a{font-size:12px;color:var(--muted);margin-top:6px;line-height:1.5}
.sign{width:22px;height:22px;border-radius:50%;background:var(--blue);color:var(--white);display:flex;align-items:center;justify-content:center;font-size:16px;line-height:1;flex:none}

/* Testimonial */
.love{height:290px;text-align:center}
.love h2{position:absolute;top:14px;width:100%;font-size:40px}
.quote{position:absolute;top:80px;left:260px;width:680px;font-style:italic;font-size:20px;line-height:1.5}
.author{position:absolute;top:160px;width:100%;font-family:'Oswald',sans-serif;font-weight:700;font-size:16px}
.role{position:absolute;top:186px;width:100%;font-size:12px;color:var(--muted)}
.arrows{position:absolute;top:220px;left:564px;display:flex;gap:12px}
.arrows span{width:32px;height:32px;border-radius:50%;background:var(--navy);display:flex;align-items:center;justify-content:center}
.arrows span.next{background:var(--blue)}

/* Footer */
.footer{height:476px;background:var(--navy)}
.footer .logo{position:absolute;left:80px;top:100px;font-size:24px}
.col{position:absolute;top:86px;color:var(--white)}
.col h3{font-size:20px;margin-bottom:16px}
.col li{list-style:none;font-size:14px;line-height:1.8;color:#d6dfe8}
.col-menu{left:448px}
.col-contact{left:640px}
.contact-row{display:flex;gap:10px;margin-bottom:10px}
.contact-row b{display:block;font-size:13px;font-weight:600}
.contact-row span{font-size:13px;color:#d6dfe8;line-height:1.5}
.col-follow{left:888px}
.socials{display:flex;gap:10px}
.socials i{width:30px;height:30px;border-radius:50%;background:var(--blue-light);display:block}
.bottom-bar{position:absolute;left:0;right:0;bottom:0;height:60px;border-top:1px solid #1c3a5c;color:#cfd9e4;font-size:13px;text-align:center;line-height:60px}
</style>
</head>
<body>

<header class="hero">
  <div class="hero-visual" role="img" aria-label="Humanoid robot working at a laptop in front of a glowing circuit background"></div>
  <nav class="nav">
    <div class="logo">KorvanPro-Mira Talk Hub</div>
    <div class="nav-links"><span>Home</span><span>About Us</span><span>Why Choose Us</span><span>Contact Us</span><span>Sign up</span></div>
    <div class="login"><i></i>Login</div>
  </nav>
  <h1>Instantly create a free AI chatbot.</h1>
  <p>for your website! Just enter the URL of your website below and the chatbot will educate itself about your business</p>
  <div class="url-box">Enter Your Website Domain URL</div>
  <span class="btn">Try It Now</span>
  <svg class="hero-curve" width="1200" height="90" viewBox="0 0 1200 90" aria-hidden="true">
    <path d="M0 90 L0 60 Q300 66 520 50 Q600 20 680 50 Q900 66 1200 60 L1200 90 Z" fill="#ffffff"/>
    <circle cx="600" cy="52" r="16" fill="none" stroke="#1ea0e6" stroke-width="2"/>
    <path d="M593 50 L600 57 L607 50" fill="none" stroke="#1ea0e6" stroke-width="2"/>
  </svg>
</header>

<section class="welcome">
  <div class="welcome-photo" role="img" aria-label="Two colleagues talking with a humanoid robot in an office"></div>
  <h2>Welcome to Mira Talk Hub</h2>
  <p>Imagine having a tireless assistant that's always ready to interact with your customers, answer their questions, and guide them through their journey on your website. Meet Mira Talk Hub, the fastest and easiest way to create an intelligent AI agent for your business in just a few minutes. Whether you're a small business owner, a growing enterprise or a digital agency, Mira Talk Hub is here to revolutionize customer support for you.</p>
  <span class="btn">Read More</span>
</section>

<section class="how">
  <h2>How it works</h2>
  <p class="lead">Enter the URL of your website, and let Mira Talk Hub do the heavy lifting. The bot will crawl your site and educate itself about your business. Choose from three crawling options:</p>
  <div class="how-cards">
    <div class="how-card"><span class="tab"></span><h3>Specific Sub-Pages</h3><p>Focus on important sections like FAQs, pricing, or services.</p></div>
    <div class="how-card"><span class="tab"></span><h3>Home Page Only</h3><p>Ideal for a quick setup with basic information.</p></div>
    <div class="how-card"><span class="tab"></span><h3>All Pages</h3><p>For a comprehensive AI assistant across your business inside out.</p></div>
  </div>
  <span class="btn">View More</span>
</section>

<section class="why">
  <h2 class="why-title">Why choose Mira Talk Hub?</h2>
  <p class="intro">Mira Talk Hub isn't just another chatbot. It's a customizable, smart, and scalable solution designed to:</p>
  <ul>
    <li>Enhance your customer support 24/7.</li>
    <li>Save your time by automating repetitive inquiries.</li>
    <li>Improve customer satisfaction and engagement.</li>
  </ul>
  <span class="btn">Read More</span>
  <div class="why-photo" role="img" aria-label="Support agent with a headset presenting a report chart"></div>
  <h2 class="plans-title">Customizable plans</h2>
  <p class="plans-sub">Mira Talk Hub is designed for businesses of all sizes</p>
  <div class="plan-cards">
    <div class="plan-card"><span class="icon"></span><h3>Free Plan</h3><p>Perfect for smaller or newer businesses.</p></div>
    <div class="plan-card"><span class="icon"></span><h3>Business Plan</h3><p>Scaled for growing enterprises with advanced features.</p></div>
    <div class="plan-card"><span class="icon"></span><h3>Agency Plan</h3><p>Allows unlimited chatbot creation for digital agencies.</p></div>
  </div>
</section>

<section class="features">
  <h2>Customizable plans</h2>
  <div class="tile tile-a" role="img" aria-label="Team reviewing chatbot alerts at a warmly lit desk">
    <div class="shade"></div>
    <h3>Real-Time Notifications</h3>
    <p>Stay on top of customer interactions with text and email alerts for new inquiries. Never miss a chance to connect.</p>
  </div>
  <div class="tile tile-b" role="img" aria-label="Person checking the chatbot on a mobile phone">
    <div class="shade"></div>
    <h3>Mobile App Access</h3>
    <p>Monitor your bot's activity and interact with customers directly through our mobile app, whether you're at a meeting.</p>
  </div>
</section>

<section class="try">
  <div class="try-photo" role="img" aria-label="Friendly robots at work in a bright modern room"></div>
  <h2>Try Mira Talk Hub now it's free!</h2>
  <p class="p1">Are you ready to elevate your business with the power of AI? Getting started is as easy as entering your website URL into the box below. Within minutes, your AI assistant will be ready to take your customer support to the next level.</p>
  <p class="p2">Don't wait to experience the future of customer interaction. Try Mira Talk Hub now for free and watch your business grow effortlessly. Click the button below to start your journey.</p>
  <span class="btn">Learn More</span>
</section>

<section class="faq">
  <h2>FAQs</h2>
  <div class="faq-list">
    <div class="faq-item open">
      <div class="faq-q">Q: How long does it take to set up Mira Talk Hub? <span class="sign">−</span></div>
      <p class="faq-a">A: You can have your Mira Talk Hub live on your website in just a few minutes. The setup process is quick and user-friendly.</p>
    </div>
    <div class="faq-item"><span class="faq-q">Q: Is there a free plan available?</span><span class="sign">+</span></div>
    <div class="faq-item"><span class="faq-q">Q: Can I add my own content to the bot's knowledge base?</span><span class="sign">+</span></div>
    <div class="faq-item"><span class="faq-q">Q: What if I want to interact directly with some customers without the bot's assistance?</span><span class="sign">+</span></div>
  </div>
</section>

<section class="love">
  <h2>Why businesses love Mira Talk Hub</h2>
  <p class="quote">“Mira Talk Hub transformed our customer support. It's like having an extra team member who works 24/7!”</p>
  <p class="author">LENA V</p>
  <p class="role">Small Business Owner</p>
  <div class="arrows">
    <span><svg width="12" height="12" viewBox="0 0 12 12"><path d="M8 2 L4 6 L8 10" fill="none" stroke="#fff" stroke-width="2"/></svg></span>
    <span class="next"><svg width="12" height="12" viewBox="0 0 12 12"><path d="M4 2 L8 6 L4 10" fill="none" stroke="#fff" stroke-width="2"/></svg></span>
  </div>
</section>

<footer class="footer">
  <div class="logo">KorvanPro-Mira Talk Hub</div>
  <div class="col col-menu">
    <h3>Menu</h3>
    <ul><li>Home</li><li>About Us</li><li>Why Choose Us</li><li>Contact Us</li></ul>
  </div>
  <div class="col col-contact">
    <h3>Contact Us</h3>
    <div class="contact-row">
      <svg width="16" height="16" viewBox="0 0 16 16"><path d="M3 1 L6 1 L7 5 L5 6 Q6 9 10 11 L11 9 L15 10 L15 13 Q14 15 12 15 Q2 13 1 3 Q1 1 3 1Z" fill="#43b8f2"/></svg>
      <div><b>Phone</b><span>+00 555 0142 88</span></div>
    </div>
    <div class="contact-row">
      <svg width="16" height="16" viewBox="0 0 16 16"><rect x="1" y="3" width="14" height="10" rx="2" fill="#43b8f2"/><path d="M1 4 L8 9 L15 4" fill="none" stroke="#061a33" stroke-width="1.4"/></svg>
      <div><b>Email</b><span>hello@miratalkhub.co</span></div>
    </div>
    <div class="contact-row">
      <svg width="16" height="16" viewBox="0 0 16 16"><path d="M8 1 Q13 1 13 6 Q13 10 8 15 Q3 10 3 6 Q3 1 8 1Z" fill="#43b8f2"/><circle cx="8" cy="6" r="2" fill="#061a33"/></svg>
      <div><b>Location</b><span>27 Harbor Lane, Suite 400<br>Bay City 2000</span></div>
    </div>
  </div>
  <div class="col col-follow">
    <h3>Follow Us</h3>
    <div class="socials"><i></i><i></i><i></i><i></i></div>
  </div>
  <div class="bottom-bar">KorvanPro © 2025 Privacy Policy Terms of Use</div>
</footer>

</body>
</html>
```